Virtual Personal Training Flyer Design

We are a virtual personal training website, acting as the intermediary between the customer and the personal trainer. The customer can choose their personal trainer based on specialty and then subscribe and have access to their videos, training nutritional advice and live sessions.
We have sent over an orange and blue background for inspiration of the theme and also our three logos. Kestrel Fitness is the company and KestrelMXR is the product and the F is our standard logo.
We want our social media links on the flyer which are Twitter: @KestrelMXR and Facebook: KestrelMXR. We also want our e-mail address which is kestrelmxr@quillpost.net and telephone number which is 07516290347.

We also want to put the key benefits for consumers onto the flyers, which are wide variety of personal trainers to choose from and tailored to you, have constant access to videos etc, save time travelling to the gym, saving effort - more convenient, cheaper than personal training in the gym - saving money, gain from trainer's knowledge - more informed about workout and what exercises you are doing etc. We would like to add rhetorical questions such as Want a personal trainer but can't afford one? or Want to have a structured training program but haven't got the time or access to a gym?
We also want our slogan on there which is MXR, step into the self you've long been chasing.

women aged between 18 and 35

Personal Trainer

• don't want old fonts or clash colours and shouldn't be cartooney.

```html
<!DOCTYPE html>
<html lang="en">
<head>
<meta charset="utf-8">
<title>KestrelMXR Flyer</title>
<link rel="stylesheet" href="https://fonts.googleapis.com/css2?family=Fira+Sans+Condensed:wght@400;600;700&family=Montserrat:wght@500;700;800&family=Arimo:wght@400;700&display=swap">
<style>
  :root {
    --page: #ebebeb;
    --navy: #2e3192;
    --blue: #0a6cc4;
    --blue-deep: #1b3f95;
    --orange: #f7941d;
    --white: #ffffff;
    --grass: #7fb04a;
    --grass-light: #b9d98a;
    --grass-dark: #4f7d2c;
    --skin: #e9c3a6;
    --badge: #dcdcd6;
  }
  * { margin: 0; padding: 0; box-sizing: border-box; }
  html, body { width: 1200px; height: 1000px; overflow: hidden; background: var(--page); }
  .flyer {
    position: absolute; left: 333px; top: 150px; width: 495px; height: 700px;
    background: var(--white); overflow: hidden;
    font-family: "Montserrat", sans-serif;
  }
  .header {
    position: absolute; inset: 0 0 auto 0; height: 145px;
    background: linear-gradient(180deg, var(--blue-deep) 0%, var(--blue) 45%, var(--blue-deep) 100%);
    color: var(--white); text-align: center;
    font-family: "Fira Sans Condensed", sans-serif; text-transform: uppercase;
  }
  .header .question { position: absolute; top: 23px; width: 100%; font-size: 19.5px; font-weight: 400; }
  .header .headline { position: absolute; top: 50px; width: 100%; font-size: 39px; font-weight: 700; line-height: 46px; letter-spacing: 0.6px; }

  .hero-photo {
    position: absolute; left: 0; top: 145px; width: 495px; height: 375px;
    background:
      radial-gradient(ellipse 120px 150px at 310px 150px, rgba(240,214,196,0.95) 0%, rgba(233,195,166,0.6) 45%, rgba(233,195,166,0) 100%),
      radial-gradient(ellipse 70px 120px at 240px 140px, rgba(230,225,215,0.85) 0%, rgba(230,225,215,0) 100%),
      radial-gradient(ellipse 40px 70px at 180px 40px, rgba(90,75,55,0.7) 0%, rgba(90,75,55,0) 100%),
      linear-gradient(180deg, var(--grass-light) 0%, var(--grass) 35%, var(--grass-dark) 60%, var(--grass) 80%, #c9d8b4 100%);
  }
  .brand-badge {
    position: absolute; left: 0; top: 145px; width: 160px; height: 62px;
    background: var(--badge); clip-path: polygon(0 0, 100% 0, 82% 100%, 0 100%);
    display: flex; align-items: center; padding-left: 12px;
  }
  .brand-badge span { font-family: "Arimo", sans-serif; font-weight: 700; font-size: 19px; color: var(--navy); }
  .slogan {
    position: absolute; left: 14px; top: 273px; font-family: "Arimo", sans-serif;
    font-weight: 700; font-size: 12.5px; color: var(--navy);
  }
  .benefits {
    position: absolute; left: 0; top: 348px; width: 308px; height: 72px;
    background: var(--navy); clip-path: polygon(0 0, 96% 0, 100% 100%, 0 100%);
    color: var(--white); font-family: "Arimo", sans-serif; font-size: 13px; line-height: 20px;
    padding: 7px 0 0 12px; list-style: none;
  }
  .benefit-rule { position: absolute; left: 0; top: 420px; width: 310px; height: 5px; background: var(--orange); }
  .white-ground { position: absolute; left: 0; top: 425px; width: 495px; height: 275px; background: var(--white); }

  .access-photo {
    position: absolute; left: 262px; top: 505px; width: 233px; height: 195px;
    background:
      radial-gradient(ellipse 40px 50px at 150px 60px, rgba(200,150,120,0.9) 0%, rgba(200,150,120,0) 100%),
      radial-gradient(ellipse 90px 110px at 130px 150px, rgba(60,55,55,0.85) 0%, rgba(60,55,55,0) 100%),
      radial-gradient(ellipse 60px 50px at 55px 120px, rgba(225,185,160,0.8) 0%, rgba(225,185,160,0) 100%),
      linear-gradient(135deg, rgba(255,255,255,1) 0%, #f1ede9 35%, #e3d8cf 100%);
  }
  .shapes { position: absolute; left: 0; top: 0; }
  .access-label {
    position: absolute; left: 419px; top: 416px; color: var(--white);
    font-family: "Fira Sans Condensed", sans-serif; line-height: 17px;
  }
  .access-label b { display: block; font-size: 22px; font-weight: 700; }
  .access-label span { font-size: 15px; }

  .contact { position: absolute; left: 0; top: 440px; width: 306px; text-align: center; color: var(--navy); }
  .contact .cta { font-size: 23px; font-weight: 800; letter-spacing: 0.3px; }
  .contact .cta-sub { font-size: 14px; font-weight: 700; margin-top: -2px; }
  .company-name { position: absolute; left: 75px; top: 498px; font-family: "Arimo", sans-serif; font-size: 20px; font-weight: 700; color: var(--orange); }
  .phone-icon { position: absolute; left: 28px; top: 539px; }
  .contact-box { position: absolute; left: 48px; top: 542px; width: 204px; height: 49px; border-radius: 7px; overflow: hidden; }
  .contact-box .phone {
    height: 28px; background: linear-gradient(180deg, var(--blue), var(--blue-deep));
    color: var(--white); font-weight: 700; font-size: 17px; text-align: center; line-height: 28px; letter-spacing: 0.5px;
  }
  .contact-box .email { height: 21px; background: var(--orange); color: var(--white); font-weight: 700; font-size: 11.5px; text-align: center; line-height: 21px; }
  .social-title { position: absolute; left: 0; top: 601px; width: 296px; text-align: center; color: var(--navy); font-weight: 700; font-size: 12.5px; }
  .social { position: absolute; top: 626px; display: flex; align-items: center; gap: 8px; color: var(--navy); font-family: "Arimo", sans-serif; font-size: 13px; }
  .social i { display: block; width: 20px; height: 20px; border-radius: 3px; background: var(--blue-deep); }
  .social.fb { left: 38px; }
  .social.tw { left: 156px; }
  .social.tw i { background: #4aa7d8; }
  .website { position: absolute; left: 0; top: 657px; width: 296px; text-align: center; color: var(--navy); font-weight: 700; font-size: 13px; }
</style>
</head>
<body>
<main class="flyer">
  <header class="header">
    <p class="question">Want a personal trainer but can’t afford one?</p>
    <h1 class="headline">Get a personal trainer<br>for an affordable price</h1>
  </header>

  <div class="hero-photo" role="img" aria-label="Photo of a smiling man and woman resting on the grass in a sunny park"></div>
  <div class="white-ground"></div>
  <div class="brand-badge"><span>KestrelMXR</span></div>
  <p class="slogan">“MXR, step into the self you’ve long been chasing.”</p>

  <ul class="benefits">
    <li>Access to a variety of personal trainers online</li>
    <li>Video training | &nbsp;Live sessions</li>
    <li>Expert training and nutritional advice</li>
  </ul>
  <div class="benefit-rule"></div>

  <div class="access-photo" role="img" aria-label="Photo of a woman sitting on the floor using a smartphone beside small dumbbells"></div>

  <svg class="shapes" width="495" height="700" viewBox="0 0 495 700" aria-hidden="true">
    <polygon points="495,318 495,350 308,424" fill="var(--navy)"/>
    <polygon points="308,424 495,350 495,487" fill="var(--orange)"/>
    <polygon points="308,424 495,487 495,517 350,492" fill="var(--navy)"/>
    <g fill="none" stroke="var(--white)" stroke-width="6">
      <path d="M353 424 A30 30 0 0 1 408 424"/>
      <path d="M409 452 A30 30 0 0 1 354 452"/>
    </g>
    <polygon points="400,414 416,428 398,434" fill="var(--white)"/>
    <polygon points="362,462 346,448 364,442" fill="var(--white)"/>
    <text x="381" y="448" text-anchor="middle" font-family="Fira Sans Condensed, sans-serif" font-weight="700" font-size="30" fill="var(--white)">24</text>
  </svg>
  <p class="access-label"><b>HOUR</b><span>ACCESS</span></p>

  <section class="contact">
    <h2 class="cta">CONTACT US NOW!!</h2>
    <p class="cta-sub">FOR FURTHER INFORMATION</p>
  </section>
  <p class="company-name">Kestrel Fitness</p>

  <svg class="phone-icon" width="24" height="56" viewBox="0 0 24 56" aria-hidden="true">
    <path d="M15 2 h5 a2 2 0 0 1 2 2 v9 a2 2 0 0 1 -2 2 h-5 q-4 13 0 26 h5 a2 2 0 0 1 2 2 v9 a2 2 0 0 1 -2 2 h-5 q-14 -4 -14 -26 q0 -22 14 -26z" fill="var(--navy)"/>
    <path d="M9 49 q-3 3 0 5 q3 1 2 -2" fill="none" stroke="var(--navy)" stroke-width="1.2"/>
  </svg>
  <div class="contact-box">
    <p class="phone">+44 7516 290347</p>
    <p class="email">kestrelmxr@quillpost.net</p>
  </div>

  <p class="social-title">Follow Our Social Media:</p>
  <p class="social fb"><i></i>KestrelMXR</p>
  <p class="social tw"><i></i>KestrelMXR</p>
  <p class="website">www.kestrelmxr.com</p>
</main>
</body>
</html>
```